Rigging Brochure for New Electric Crane!!!

We have purchased a new Veltra crane from Italy that will arrive in March 2020. We would like to advertise that we will be the only company in North America with this crane. This will be the highlight of the brochure.
We would also like a section that shows our other services, such as machinery moving, transportation, warehouse storage, government work etc.

We are interested in purchasing more than one design and are open to both bi-fold and tri-fold brochures.

For a bi-fold the pre-fold size is 17 x 11" so the final size of each section would be 8.5 x 11 inches.
For a tri-fold the pre-fold size would be 11 x 8.5" so each section would be 3.6 x 8.5 inches.

Target Market(s)

Industrial - power plants, machine shops, hospitals, anyone with heavy equipment that needs to be moved or stored

Font styles to use
Sans Serif

Colors
ec1f27
0255a3
ffffff

Requirements
Must have
• Main photo of Veltra crane photoshopped with our company logo on front page
• Our logo and website/contact information
• hollandhoist.example 480-555-0172
Nice to have
• pleasing arrangement of photos that create an overall professional appeal
• company colors of red, white, black, grey and blue
• social media info
• Not all photos need to be used
Should not have
• any competitor's names. All photos provided by Veltra may keep the veltra logo, but any other competitor logos need to be photoshopped out.

```html
<!DOCTYPE html>
<html lang="en">
<head>
<meta charset="utf-8">
<title>Holland Hoist – Pick and Carry Brochure</title>
<link href="https://fonts.googleapis.com/css2?family=Montserrat:wght@600;800;900&family=Open+Sans:wght@400;600;700&display=swap" rel="stylesheet">
<style>
  :root{
    --red:#ec1f27;
    --red-dark:#b3121a;
    --blue:#0255a3;
    --blue-dark:#013f7a;
    --white:#ffffff;
    --black:#141414;
    --grey:#e6e7e9;
    --grey-mid:#9a9ca0;
    --text:#3a3a3a;
    --stage:#ececee;
  }
  *{box-sizing:border-box;margin:0;padding:0}
  html,body{width:668px;height:1200px;overflow:hidden}
  body{background:var(--stage);font-family:"Open Sans",Arial,sans-serif;color:var(--text);position:relative}
  .spread{position:absolute;left:24px;width:620px;height:401px;display:flex;box-shadow:0 6px 18px rgba(0,0,0,.18);background:var(--white)}
  .spread--outside{top:150px}
  .spread--inside{top:640px}
  .panel{position:relative;width:310px;height:401px;overflow:hidden;background:var(--white)}
  .brand{position:absolute;display:flex;align-items:center;gap:4px;font-family:"Montserrat",Arial,sans-serif;font-weight:900;font-size:12px;color:var(--black);letter-spacing:.2px}
  .brand__mark{width:8px;height:8px;background:var(--red)}
  .brand--white{color:var(--white)}
  .photo{position:absolute}
  .photo--red{background:linear-gradient(135deg,#7a1216 0%,#c22a2f 45%,#5a1013 100%)}
  .photo--crane{background:linear-gradient(160deg,#c9cdd3 0%,#8f959d 40%,#b7262c 70%,#4c4f55 100%)}
  .photo--yard{background:linear-gradient(180deg,#cfd9e4 0%,#9aa3ab 55%,#5e6369 100%)}
  .photo--truck{background:linear-gradient(180deg,#d7dde3 0%,#c9a33a 55%,#6b6b6b 100%)}
  .photo--lift{background:linear-gradient(180deg,#e9eef3 0%,#c4cbd2 45%,#2f6fb0 75%,#8d9196 100%)}
  .photo--shop{background:linear-gradient(180deg,#8e9297 0%,#d9dadb 60%,#6d7075 100%)}
  .heading{font-family:"Montserrat",Arial,sans-serif;font-weight:800;font-size:11px;color:var(--black)}
  .heading .accent{color:var(--red)}
  .body-copy{font-size:5.2px;line-height:1.5;color:var(--text)}
  .web-bar{position:absolute;background:var(--black);color:var(--white);font-family:"Montserrat",Arial,sans-serif;font-weight:600;font-size:7px;display:flex;align-items:center;justify-content:center;gap:5px;border-radius:2px}
  .web-bar__dot{width:5px;height:5px;border-radius:50%;background:var(--red)}

  /* back panel */
  .about{position:absolute;left:14px;top:116px;width:282px}
  .about__rule{width:22px;height:2px;background:var(--red);margin:3px 0 5px}
  .about__list{list-style:none}
  .about__list li{font-size:5.2px;line-height:1.6;padding-left:7px;position:relative}
  .about__list li::before{content:"";position:absolute;left:0;top:2.5px;width:3px;height:3px;background:var(--red)}
  .contact{position:absolute;left:0;top:252px;width:310px;height:149px;background:var(--blue);color:var(--white);padding:14px 14px}
  .contact .heading{color:var(--white)}
  .contact .heading .accent{color:var(--white);opacity:.75}
  .contact__row{display:flex;align-items:center;gap:6px;font-size:6.5px;margin-top:6px}
  .contact__icon{width:11px;height:11px;border-radius:50%;background:var(--red);display:flex;align-items:center;justify-content:center}

  /* front panel */
  .cover__title{position:absolute;left:0;width:310px;top:268px;text-align:center;font-family:"Montserrat",Arial,sans-serif;font-weight:900;font-size:25px;color:var(--white);letter-spacing:.5px}
  .cover__sub{position:absolute;left:40px;width:230px;top:302px;text-align:center;font-size:5.5px;color:var(--white);line-height:1.5;opacity:.9}

  /* inside left */
  .intro{position:absolute;left:14px;top:44px;width:190px}
  .services{position:absolute;left:14px;top:92px;display:flex;gap:9px}
  .service{width:48px;text-align:center}
  .service__label{font-size:4.8px;font-weight:700;color:var(--black);margin-top:2px;line-height:1.25}
  .caption{position:absolute;font-family:"Montserrat",Arial,sans-serif;font-weight:800;font-size:6px;color:var(--white);background:var(--red);padding:2px 5px}

  /* inside right */
  .block{position:absolute;left:12px;width:170px}
  .block__head{display:inline-block;background:var(--black);color:var(--white);font-family:"Montserrat",Arial,sans-serif;font-weight:800;font-size:6px;padding:2px 6px;margin-bottom:3px}
  .phone-box{position:absolute;right:14px;bottom:10px;background:var(--white);color:var(--black);font-family:"Montserrat",Arial,sans-serif;font-weight:800;font-size:8px;padding:4px 8px;display:flex;align-items:center;gap:5px;border-radius:2px}
</style>
</head>
<body>

<!-- Outside spread: back panel + front cover -->
<section class="spread spread--outside">
  <article class="panel panel--back">
    <div class="brand" style="left:14px;top:12px"><span class="brand__mark"></span>Holland Hoist</div>
    <div class="photo photo--red" style="left:0;top:36px;width:310px;height:72px" role="img" aria-label="Red-toned photo of cranes and rigging equipment in the yard"></div>
    <svg style="position:absolute;left:0;top:36px" width="310" height="72" viewBox="0 0 310 72"><path d="M0 60 L120 72 L0 72Z" fill="#fff"/><path d="M310 50 L190 72 L310 72Z" fill="#fff"/></svg>
    <div class="about">
      <div class="heading">ABOUT <span class="accent">US</span></div>
      <div class="about__rule"></div>
      <ul class="about__list">
        <li>Family owned rigging and heavy hauling specialists serving the Southwest for decades.</li>
        <li>Machinery moving, plant relocation and precision setting of sensitive equipment.</li>
        <li>Secure warehouse storage with climate control and round the clock monitoring.</li>
        <li>Certified crews for government, hospital and power plant projects nationwide.</li>
        <li>Specialised transport, crane service and full turnkey project management.</li>
      </ul>
    </div>
    <div class="photo photo--red" style="left:0;top:208px;width:310px;height:44px" role="img" aria-label="Red-toned photo of a crane lifting machinery"></div>
    <div class="brand brand--white" style="left:14px;top:223px"><span class="brand__mark" style="background:var(--white)"></span>Holland Hoist</div>
    <div class="contact">
      <div class="heading">CONTACT <span class="accent">US</span></div>
      <div class="contact__row">
        <span class="contact__icon"><svg width="7" height="7" viewBox="0 0 24 24"><path fill="#fff" d="M6.6 10.8a15 15 0 006.6 6.6l2.2-2.2a1 1 0 011-.25 11.4 11.4 0 003.6.6 1 1 0 011 1V20a1 1 0 01-1 1A17 17 0 013 4a1 1 0 011-1h3.5a1 1 0 011 1c0 1.25.2 2.45.6 3.6a1 1 0 01-.25 1z"/></svg></span>
        480-555-0172
      </div>
      <div class="contact__row">
        <span class="contact__icon"><svg width="7" height="7" viewBox="0 0 24 24"><path fill="#fff" d="M12 2a7 7 0 00-7 7c0 5 7 13 7 13s7-8 7-13a7 7 0 00-7-7zm0 9.5A2.5 2.5 0 1112 6.5a2.5 2.5 0 010 5z"/></svg></span>
        1200 Industrial Way, Mesa, AZ 85201
      </div>
      <div class="contact__row">
        <span class="contact__icon"><svg width="7" height="7" viewBox="0 0 24 24"><path fill="#fff" d="M2 5h20v14H2z M2 5l10 8 10-8" stroke="#fff" stroke-width="1" fill="none"/></svg></span>
        info@hollandhoist.example
      </div>
    </div>
    <div class="web-bar" style="left:60px;top:372px;width:190px;height:15px"><span class="web-bar__dot"></span>www.hollandhoist.example</div>
  </article>

  <article class="panel panel--front">
    <div class="brand" style="left:16px;top:12px"><span class="brand__mark"></span>Holland Hoist</div>
    <div class="photo photo--crane" style="left:0;top:36px;width:310px;height:220px" role="img" aria-label="Photo of the new red electric pick and carry crane in front of an industrial building"></div>
    <svg style="position:absolute;left:0;top:226px" width="310" height="175" viewBox="0 0 310 175">
      <path d="M0 30 Q155 -10 310 20 L310 175 L0 175Z" fill="#fff"/>
      <path d="M0 36 Q155 -4 310 26 L310 175 L0 175Z" fill="var(--blue)"/>
      <path d="M0 150 L310 120 L310 175 L0 175Z" fill="var(--blue-dark)"/>
    </svg>
    <div class="cover__title">PICK AND CARRY</div>
    <div class="cover__sub">The only electric pick and carry crane of its kind in North America, arriving March 2020 and ready for your next lift.</div>
    <div class="web-bar" style="left:60px;top:360px;width:190px;height:15px"><span class="web-bar__dot"></span>www.hollandhoist.example</div>
  </article>
</section>

<!-- Inside spread -->
<section class="spread spread--inside">
  <article class="panel panel--inside-left">
    <svg style="position:absolute;right:0;top:0" width="140" height="40" viewBox="0 0 140 40"><path d="M20 0 Q70 40 140 30 L140 0Z" fill="var(--red)"/></svg>
    <div class="brand" style="left:14px;top:12px"><span class="brand__mark"></span>Holland Hoist</div>
    <div class="intro">
      <div class="heading" style="font-size:8px">OUR <span class="accent">SERVICES</span></div>
      <p class="body-copy" style="margin-top:3px">From single machines to entire plants, our crews plan, rig, move and store your equipment safely and on schedule.</p>
    </div>
    <div class="services">
      <div class="service"><svg width="30" height="34" viewBox="0 0 30 34"><path d="M15 1 L29 9 L29 25 L15 33 L1 25 L1 9Z" fill="var(--red)"/><circle cx="15" cy="17" r="5" fill="none" stroke="#fff" stroke-width="2"/></svg><div class="service__label">Machinery Moving</div></div>
      <div class="service"><svg width="30" height="34" viewBox="0 0 30 34"><path d="M15 1 L29 9 L29 25 L15 33 L1 25 L1 9Z" fill="var(--red)"/><rect x="9" y="12" width="12" height="9" fill="none" stroke="#fff" stroke-width="2"/></svg><div class="service__label">Transport</div></div>
      <div class="service"><svg width="30" height="34" viewBox="0 0 30 34"><path d="M15 1 L29 9 L29 25 L15 33 L1 25 L1 9Z" fill="var(--red)"/><path d="M8 22 L8 14 L15 10 L22 14 L22 22Z" fill="none" stroke="#fff" stroke-width="2"/></svg><div class="service__label">Warehouse Storage</div></div>
      <div class="service"><svg width="30" height="34" viewBox="0 0 30 34"><path d="M15 1 L29 9 L29 25 L15 33 L1 25 L1 9Z" fill="var(--red)"/><path d="M10 17 L14 21 L21 12" fill="none" stroke="#fff" stroke-width="2"/></svg><div class="service__label">Government Work</div></div>
      <div class="service"><svg width="30" height="34" viewBox="0 0 30 34"><path d="M15 1 L29 9 L29 25 L15 33 L1 25 L1 9Z" fill="var(--red)"/><path d="M11 23 L11 10 L21 10 M21 10 L21 16" fill="none" stroke="#fff" stroke-width="2"/></svg><div class="service__label">Crane Service</div></div>
    </div>
    <div class="photo photo--shop" style="left:14px;top:150px;width:135px;height:82px" role="img" aria-label="Photo of crew moving machinery inside a plant"></div>
    <div class="caption" style="left:14px;top:232px">MACHINERY MOVING</div>
    <div class="photo photo--yard" style="left:160px;top:150px;width:136px;height:82px" role="img" aria-label="Photo of equipment stored in the warehouse"></div>
    <div class="caption" style="left:160px;top:232px">WAREHOUSE STORAGE</div>
    <p class="body-copy" style="position:absolute;left:14px;top:250px;width:282px">Our trained riggers handle presses, generators, medical imaging units and more with the right gear for every lift.</p>
    <svg style="position:absolute;left:0;top:280px" width="310" height="121" viewBox="0 0 310 121"><path d="M0 20 L310 0 L310 121 L0 121Z" fill="var(--red)"/></svg>
    <div class="photo photo--truck" style="left:14px;top:300px;width:135px;height:82px" role="img" aria-label="Photo of a heavy haul truck carrying equipment"></div>
    <div class="block" style="left:160px;top:304px;width:136px">
      <span class="block__head">TRANSPORTATION</span>
      <p class="body-copy" style="color:var(--white)">Flatbeds, lowboys and step decks for oversized and heavy loads across the region.</p>
    </div>
  </article>

  <article class="panel panel--inside-right">
    <div class="block" style="top:14px">
      <span class="block__head">GOVERNMENT WORK</span>
      <p class="body-copy">Approved contractor for federal, state and municipal projects with full compliance.</p>
    </div>
    <div class="photo photo--yard" style="left:196px;top:12px;width:100px;height:52px" role="img" aria-label="Photo of a crane on a government job site"></div>
    <div class="block" style="top:76px">
      <span class="block__head">CRANE SERVICE</span>
      <p class="body-copy">Mobile and pick and carry cranes with certified operators for tight indoor lifts.</p>
    </div>
    <div class="photo photo--truck" style="left:196px;top:74px;width:100px;height:52px" role="img" aria-label="Photo of a yellow mobile crane"></div>
    <div class="block" style="top:138px">
      <span class="block__head">PROJECT PLANNING</span>
      <p class="body-copy">Site surveys, lift plans and scheduling so your move runs on time and on budget.</p>
    </div>
    <div class="photo photo--shop" style="left:196px;top:136px;width:100px;height:52px" role="img" aria-label="Photo of rigging crew planning a lift"></div>
    <div class="photo photo--lift" style="left:12px;top:200px;width:286px;height:150px" role="img" aria-label="Photo of the electric pick and carry crane lifting a load"></div>
    <svg style="position:absolute;left:0;top:350px" width="310" height="51" viewBox="0 0 310 51"><path d="M0 12 L310 0 L310 51 L0 51Z" fill="var(--red)"/></svg>
    <div class="phone-box">
      <svg width="8" height="8" viewBox="0 0 24 24"><path fill="var(--red)" d="M6.6 10.8a15 15 0 006.6 6.6l2.2-2.2a1 1 0 011-.25 11.4 11.4 0 003.6.6 1 1 0 011 1V20a1 1 0 01-1 1A17 17 0 013 4a1 1 0 011-1h3.5a1 1 0 011 1c0 1.25.2 2.45.6 3.6a1 1 0 01-.25 1z"/></svg>
      480-555-0172
    </div>
  </article>
</section>

</body>
</html>
```